I have a PHP web application to manage IT support calls and require a front-end design and user logon screen.

I have attached the current design which needs improving.

I have 2 current designs. The 2nd design is one I have been working on but requires a "professional touch". I also require the tables designed with dummy data from the 1st design.

I have attached my company logo in AI format which I would like incorporated into the design. There should also be a placeholder to supply the users company name upon login.

The screenshots I have attached should explain what I am looking for.

The Home Page should include charts which show statistical information such as:
Number of support tickets logged per month. Bar Chart etc.
Number of currently open support tickets.
Number of Quote Requests awaiting a response.
Number of Files and file repository.
Number of Reports.
Number of Customers.

For the Jobs and Customers pages the table fields should be designed as per the attached screenshots but a better looking tables. The table options such as uploading a file and adding a customer - these options can be changed and displayed differently.

Quotes page should display quotes returned and a "request a quote form".

Files page should have a good structure for browsing through an archive of files.

Profile page should have the option to include a profile picture.

An additional side page should be created for a web based calendar (these calendar entries will be updated by code).

The navbar should also include an alerts section.
The current attached design I have is based on bootstraps navbar.

Inspiration: http://plenvaro.com/freebie/free-admin-templates-for-backend-panels/

Hopefully this above link will show you some navigation style designs that I am looking for.

Please note, I will be doing the PHP coding myself and it is just the page designs I require in either HTML and or PHP format. I also require the CSS files for this project.
I need the code in a format where I can add and remove items in the menu from the code and not PSD/image based format.

If you think this project requires a higher budget let me know what you would expect and I will increase it!

Any questions, please let me know.
Dummy data can be shown for design purposes.

I have provided you a dummy login to our current system to show you the system:
https://reef.vomilbrixtonsolutions.co.uk/
username: dan.hollow@vomilbrixtonsolutions.co.uk
password:K#72zqTm

```html
<!DOCTYPE html>
<html lang="en">
<head>
<meta charset="utf-8">
<title>Files – Vomil Brixton</title>
<link rel="stylesheet" href="https://fonts.googleapis.com/css2?family=Open+Sans:wght@300;400;600&display=swap">
<style>
:root{
  --ink:#222;
  --ink-soft:#444;
  --muted:#888;
  --line:#d9d9d9;
  --line-soft:#e6e6e6;
  --side-bg:#f5f5f5;
  --white:#fff;
  --accent:#0a84ff;
  --brand:#1f4e9a;
  --folder:#f2c14e;
  --folder-dark:#d9a22c;
  --icon:#8a8a8a;
  --panel-head-top:#fbfbfd;
  --panel-head-bottom:#e9e9f1;
}
*{box-sizing:border-box;margin:0;padding:0}
html,body{width:1200px;height:840px;overflow:hidden}
body{font-family:"Open Sans",Arial,sans-serif;color:var(--ink);background:var(--white);position:relative}

.topbar{position:absolute;left:0;top:0;width:1200px;height:60px;background:var(--white);border-bottom:1px solid var(--line)}
.brand{position:absolute;left:26px;top:12px;display:flex;align-items:center;gap:8px}
.brand-dot{width:34px;height:34px;border:2px solid var(--brand);border-radius:50%}
.brand-name{font-size:18px;font-weight:600;color:var(--brand)}
.user-menu{position:absolute;left:936px;top:19px;font-size:18px;color:var(--ink)}
.user-menu::after{content:"";display:inline-block;margin-left:13px;vertical-align:middle;border:4px solid transparent;border-top:6px solid var(--ink);border-bottom:0}
.help-link{position:absolute;left:1138px;top:19px;font-size:18px;color:var(--ink)}

.sidebar{position:absolute;left:0;top:60px;width:216px;height:780px;background:var(--side-bg);border-right:1px solid var(--line)}
.nav{list-style:none;position:absolute;top:55px;left:0;width:215px}
.nav-item{position:relative;height:44.4px;display:flex;align-items:center;padding-left:55px;font-size:14px;color:var(--ink);border-bottom:1px solid var(--line-soft)}
.nav-item:first-child{border-top:1px solid var(--line-soft)}
.nav-item svg{position:absolute;left:19px;top:50%;transform:translateY(-50%)}
.nav-item.is-active{background:var(--accent);color:var(--white);border-color:var(--accent)}
.nav-item.is-active::after{content:"";position:absolute;right:-11px;top:50%;transform:translateY(-50%);border:11px solid transparent;border-left:11px solid var(--accent);border-right:0}

.page-title{position:absolute;left:216px;top:60px;width:984px;height:55px;background:var(--side-bg);border-bottom:1px solid var(--line);padding-left:24px;font-size:30px;font-weight:300;line-height:52px}

.panel{position:absolute;left:242px;top:150px;width:929px;height:326px;border:1px solid var(--line-soft);background:var(--white)}
.panel-head{height:49px;border-bottom:1px solid var(--line);background:linear-gradient(var(--panel-head-top),var(--panel-head-bottom));padding-left:13px;font-size:24px;font-weight:300;line-height:46px}
.select{position:absolute;top:62px;height:31px;border:1px solid var(--line);padding-left:8px;font-size:16px;line-height:28px;background:var(--white)}
.select::after{content:"";position:absolute;right:10px;top:13px;border:4px solid transparent;border-top:5px solid var(--ink-soft);border-bottom:0}
.select-month{left:703px;width:89px}
.select-period{left:811px;width:97px}

.tree{position:absolute;left:0;top:96px;width:227px;height:209px;border-right:1px solid var(--line)}
.tree-root{position:absolute;left:14px;top:4px;display:flex;align-items:center;font-size:16px;font-weight:600}
.tree-root::before{content:"";border:4px solid transparent;border-top:5px solid #bbb;margin-right:10px;margin-top:4px}
.tree-root svg{margin-right:13px}
.tree-branch{position:absolute;left:17px;top:30px;width:1px;height:128px;background:var(--line)}
.tree-leaf{position:absolute;left:17px;display:flex;align-items:center;font-size:16px;color:var(--ink-soft)}
.tree-leaf::before{content:"";width:30px;height:1px;background:var(--line);margin-right:17px}
.tree-leaf svg{margin-right:15px}

.folder{position:absolute;display:flex;align-items:center;font-size:16px;color:var(--ink-soft)}
.folder svg{margin-right:14px}

.footer{position:absolute;left:216px;top:799px;width:984px;height:41px;background:var(--side-bg);border-top:1px solid var(--line);text-align:center;font-size:12px;line-height:38px;color:var(--ink)}
</style>
</head>
<body>
<svg width="0" height="0" style="position:absolute">
  <defs>
    <symbol id="folder" viewBox="0 0 26 36">
      <path d="M2 3h8l2 3h12v28H2z" fill="var(--folder-dark)"/>
      <path d="M2 7l14-5v32L2 34z" fill="var(--folder)"/>
      <path d="M16 2l0 32 8 0V6z" fill="#f7d274"/>
    </symbol>
    <symbol id="file" viewBox="0 0 16 20">
      <path d="M0 0h10l6 6v14H0z" fill="var(--icon)"/>
      <path d="M10 0v6h6z" fill="#bbb"/>
    </symbol>
  </defs>
</svg>

<header class="topbar">
  <div class="brand"><span class="brand-dot"></span><span class="brand-name">Vomil Brixton</span></div>
  <div class="user-menu">Martin Fellowes</div>
  <div class="help-link">Help</div>
</header>

<aside class="sidebar">
  <ul class="nav">
    <li class="nav-item"><svg width="16" height="14" viewBox="0 0 16 14"><path d="M8 0l8 7h-2v7h-4V9H6v5H2V7H0z" fill="var(--ink)"/></svg>Home</li>
    <li class="nav-item is-active"><svg width="14" height="14" viewBox="0 0 14 14"><path d="M1 1l12 12M13 1L1 13" stroke="#fff" stroke-width="2.4"/></svg>Jobs</li>
    <li class="nav-item"><svg width="12" height="13" viewBox="0 0 12 13"><circle cx="6" cy="4" r="3.5" fill="var(--ink)"/><path d="M0 13c0-4 3-5 6-5s6 1 6 5z" fill="var(--ink)"/></svg>Customers</li>
    <li class="nav-item"><svg width="16" height="14" viewBox="0 0 16 14"><rect x="0" y="1" width="16" height="13" fill="#c9d6ee"/></svg>Inventory</li>
    <li class="nav-item"><svg width="14" height="14" viewBox="0 0 14 14"><path d="M0 2h2v12H0zM4 5h2v9H4zM8 8h2v6H8zM12 11h2v3h-2z" fill="var(--ink)"/></svg>Reports</li>
    <li class="nav-item"><svg width="12" height="15" viewBox="0 0 16 20"><path d="M0 0h10l6 6v14H0z" fill="var(--ink)"/></svg>Files</li>
    <li class="nav-item"><svg width="14" height="11" viewBox="0 0 14 11"><path d="M0 5c0-3 2-5 5-5v2C3 2 2 4 2 5h3v6H0zM8 5c0-3 2-5 5-5v2c-2 0-3 2-3 3h3v6H8z" fill="var(--ink)"/></svg>Quotes</li>
  </ul>
</aside>

<h1 class="page-title">Files</h1>

<section class="panel">
  <h2 class="panel-head">Files Repository</h2>
  <div class="select select-month">May</div>
  <div class="select select-period">Monthly</div>

  <div class="tree">
    <div class="tree-root"><svg width="20" height="22" viewBox="0 0 20 22"><ellipse cx="10" cy="4" rx="10" ry="4" fill="var(--icon)"/><path d="M0 7c0 2 4 4 10 4s10-2 10-4v5c0 2-4 4-10 4S0 14 0 12zM0 15c0 2 4 4 10 4s10-2 10-4v3c0 2-4 4-10 4S0 20 0 18z" fill="var(--icon)"/></svg>Repository</div>
    <div class="tree-branch"></div>
    <div class="tree-leaf" style="top:56px"><svg width="16" height="20"><use href="#file"/></svg>Proin tincidunt</div>
    <div class="tree-leaf" style="top:100px"><svg width="16" height="20"><use href="#file"/></svg>Donec est</div>
    <div class="tree-leaf" style="top:145px"><svg width="16" height="20"><use href="#file"/></svg>Curabitur</div>
  </div>

  <div class="folder" style="left:253px;top:117px"><svg width="26" height="36"><use href="#folder"/></svg>Morbi tristique</div>
  <div class="folder" style="left:502px;top:117px"><svg width="26" height="36"><use href="#folder"/></svg>Aliquam fringilla</div>
  <div class="folder" style="left:749px;top:117px"><svg width="26" height="36"><use href="#folder"/></svg>Tristique</div>
  <div class="folder" style="left:253px;top:181px"><svg width="26" height="36"><use href="#folder"/></svg>Enim eu elit</div>
  <div class="folder" style="left:502px;top:181px"><svg width="26" height="36"><use href="#folder"/></svg>Justo placerat</div>
  <div class="folder" style="left:749px;top:181px"><svg width="26" height="36"><use href="#folder"/></svg>Morbi</div>
  <div class="folder" style="left:253px;top:244px"><svg width="26" height="36"><use href="#folder"/></svg>posuere lectus</div>
  <div class="folder" style="left:502px;top:244px"><svg width="26" height="36"><use href="#folder"/></svg>Cum sociis</div>
</section>

<footer class="footer">Copyright © 2014 Reef</footer>
</body>
</html>
```